Velvet Lantern rebranding my business with a new business card

I have my new logo and now I need a refresher on my business cards. I really want something fun and fresh. I like black background or anything to make the color pop.
Logo
Name: Velvet Lantern
Contact Info as stated below:
Mara Pelkin
519-555-0147
Logo
Name: Velvet Lantern
Mara Pelkin
519-555-0147
fb.me/VelvetLanternbyMara
Instagram: @VelvetLanternbyMara

Industry/Entity Type

Business

Contact Information for Business Card

double-sided. Logo on one side. Contact info on the other.

Requirements
Must have
• Logo
• Name: Velvet Lantern
• Contact Info as stated below:
• Mara Pelkin
• 519-555-0147
• fb.me/VelvetLanternbyMara
• fb.me/VelvetLanternbyMara

```html
<!DOCTYPE html>
<html lang="en">
<head>
<meta charset="utf-8">
<title>Velvet Lantern – Business Card</title>
<link rel="stylesheet" href="https://fonts.googleapis.com/css2?family=Delius&display=swap">
<style>
  :root {
    --page-bg: #e4e4e4;
    --card-pink: #f4b6b8;
    --card-white: #f6f6f6;
    --ring-black: #1c1c1c;
    --ring-pink: #e79aa6;
    --badge-white: #fbf8f8;
    --ink: #222222;
    --accent: #9b3f86;
    --card-radius: 13px;
  }
  * { margin: 0; padding: 0; box-sizing: border-box; }
  html, body {
    width: 1200px;
    height: 576px;
    overflow: hidden;
    background: var(--page-bg);
    font-family: "Delius", cursive;
    color: var(--ink);
  }
  .canvas {
    position: relative;
    width: 1200px;
    height: 576px;
  }
  .card {
    position: absolute;
    top: 138px;
    height: 294px;
    border-radius: var(--card-radius);
    overflow: hidden;
  }
  .card--front {
    left: 82px;
    width: 484px;
    background: var(--card-pink);
  }
  .card--back {
    left: 602px;
    width: 482px;
    background: var(--card-white);
  }
  .card__pattern {
    position: absolute;
    inset: 0;
    background: var(--card-pink);
  }
  .card__pattern--light { background: var(--card-white); }

  .badge {
    position: absolute;
    left: 242px;
    top: 146px;
    width: 212px;
    height: 212px;
    margin: -106px 0 0 -106px;
    border-radius: 50%;
    background: var(--badge-white);
    border: 2px solid var(--ring-black);
    display: flex;
    align-items: center;
    justify-content: center;
  }
  .badge::before {
    content: "";
    position: absolute;
    inset: 5px;
    border-radius: 50%;
    border: 1.5px solid var(--ring-pink);
  }
  .brand-name {
    position: relative;
    font-size: 26px;
    color: var(--ink);
    text-align: center;
    line-height: 1.1;
  }
  .card--back .brand-name {
    position: absolute;
    left: 0;
    right: 0;
    top: 72px;
    font-size: 30px;
  }
  .holder-name {
    position: absolute;
    left: 0;
    right: 0;
    top: 203px;
    text-align: center;
    font-size: 24px;
    color: var(--ink);
  }
  .contact {
    position: absolute;
    left: 23px;
    right: 24px;
    top: 246px;
    display: flex;
    justify-content: space-between;
    align-items: center;
    font-size: 16px;
  }
  .contact__item {
    display: flex;
    align-items: center;
    gap: 9px;
  }
  .contact__icon {
    width: 19px;
    height: 19px;
    flex: none;
  }
  .contact__square {
    width: 17px;
    height: 17px;
    border: 1.5px solid var(--accent);
    border-radius: 3px;
    flex: none;
  }
</style>
</head>
<body>
<main class="canvas">

  <section class="card card--front" aria-label="Card front">
    <div class="card__pattern" role="img" aria-label="Soft pink background with faint polka dot pattern"></div>
    <div class="badge">
      <span class="brand-name">Velvet<br>Lantern</span>
    </div>
  </section>

  <section class="card card--back" aria-label="Card back">
    <div class="card__pattern card__pattern--light" role="img" aria-label="White background with faint polka dot pattern"></div>
    <span class="brand-name">Velvet Lantern</span>
    <p class="holder-name">Mara Pelkin</p>
    <div class="contact">
      <span class="contact__item">
        <svg class="contact__icon" viewBox="0 0 20 20" aria-hidden="true">
          <rect x="1" y="1" width="18" height="18" rx="4" fill="none" stroke="var(--accent)" stroke-width="1.5"/>
          <path d="M6.2 5.2c.5-.4 1.1-.3 1.4.2l1 1.6c.3.5.2 1-.2 1.3l-.6.5c.6 1.3 1.5 2.2 2.8 2.8l.5-.6c.3-.4.9-.5 1.3-.2l1.6 1c.5.3.6.9.2 1.4l-.7.8c-.5.5-1.3.7-2 .4-2.8-1.1-4.8-3.1-5.9-5.9-.3-.7-.1-1.5.4-2z" fill="var(--accent)"/>
        </svg>
        519-555-0147
      </span>
      <span class="contact__item">
        <span class="contact__square" aria-hidden="true"></span>
        VelvetLanternbyMara
      </span>
    </div>
  </section>

</main>
</body>
</html>
```